Building Certification Company needs a professional letterhead and report template

We are a modern company within an ageing industry. Our industry is responsible for life safety aspects of the built environment, we ensure buildings are safe and fit for occupation.

We use letterhead and reports everyday, we need a smart and professional letterhead that reflects the serious nature of the work we do. We also require a report template of the same ilk.

Target Market(s)

Our target market will consist mainly of professional architects, developers and construction companies.

Industry/Entity Type

Industry

Requirements
Must have
• The letterhead must have:-
Our logo
Our company details, including address, website, email, phone

Address - Suite 208 / 45 Harwick Lane Dunmore NSW 2100

Website - www.quillstonecompliance.example.au

Email - info@qsc.example.au

Phone - 02 5550 3846

The report template must have:-
A title page, which is to incorporate our logo or an aspect of our logo, get creative people.

```html
<!DOCTYPE html>
<html lang="en">
<head>
<meta charset="utf-8">
<title>Quillstone Compliance — Letterhead and Report Cover</title>
<link rel="stylesheet" href="https://fonts.googleapis.com/css2?family=Source+Sans+3:wght@400;600&display=swap">
<style>
  :root {
    --canvas: #ffffff;
    --paper: #ffffff;
    --slate: #5f707b;
    --slate-light: #aab4bb;
    --brand-blue: #4a63ad;
    --brand-navy: #2e3d91;
    --shadow: rgba(0, 0, 0, 0.35);
  }
  * { box-sizing: border-box; margin: 0; padding: 0; }
  html, body {
    width: 1200px;
    height: 806px;
    overflow: hidden;
    background: var(--canvas);
    font-family: "Source Sans 3", "Helvetica Neue", Arial, sans-serif;
  }
  .canvas {
    position: relative;
    width: 1200px;
    height: 806px;
  }
  .sheet {
    position: absolute;
    top: 48px;
    width: 506px;
    height: 714px;
    background: var(--paper);
    box-shadow: 0 2px 8px var(--shadow);
    overflow: hidden;
  }
  .sheet--letterhead { left: 65px; }
  .sheet--cover { left: 635px; }

  /* Letterhead header */
  .header-band {
    position: absolute;
    top: 47px;
    height: 25px;
    display: flex;
    flex-direction: column;
    justify-content: center;
    color: #ffffff;
    font-size: 6.3px;
    font-weight: 600;
    line-height: 1.3;
    white-space: nowrap;
  }
  .header-band--address {
    left: 0;
    width: 212px;
    padding-right: 24px;
    text-align: right;
    background: linear-gradient(90deg, var(--slate) 0%, var(--slate) 55%, var(--slate-light) 100%);
  }
  .header-band--contact {
    left: 298px;
    width: 208px;
    padding-left: 18px;
    text-align: left;
    background: linear-gradient(90deg, #ffffff 0%, #8d9fd2 12%, var(--brand-blue) 45%, var(--brand-blue) 100%);
  }
  .brand-square {
    position: absolute;
    left: 233px;
    top: 38px;
    width: 40px;
    height: 40px;
    background: var(--brand-blue);
  }

  .brand-name {
    position: absolute;
    left: 0;
    width: 100%;
    text-align: center;
    color: var(--brand-navy);
    font-weight: 600;
    text-transform: uppercase;
    line-height: 1;
  }
  .brand-name__line { display: block; }
  .brand-name--letterhead { top: 101px; }
  .brand-name--letterhead .brand-name__line--main { font-size: 21px; letter-spacing: 2.2px; }
  .brand-name--letterhead .brand-name__line--sub { font-size: 8.5px; font-weight: 400; letter-spacing: 4.4px; margin-top: 3px; }

  /* Report cover */
  .cover-graphic {
    position: absolute;
    left: 0;
    top: 54px;
    width: 506px;
    height: 607px;
    background: linear-gradient(200deg, var(--slate) 0%, var(--slate) 35%, var(--brand-blue) 65%, var(--brand-blue) 100%);
  }
  .brand-name--cover { top: 338px; color: #ffffff; }
  .brand-name--cover .brand-name__line--main { font-size: 26px; letter-spacing: 2.6px; }
  .brand-name--cover .brand-name__line--sub { font-size: 10px; font-weight: 400; letter-spacing: 5px; margin-top: 5px; }
</style>
</head>
<body>
  <main class="canvas">
    <section class="sheet sheet--letterhead" aria-label="Letterhead">
      <div class="header-band header-band--address">
        <span>Suite 208 / 45 Harwick Lane Dunmore NSW 2100</span>
        <span>02 5550 3846</span>
      </div>
      <div class="brand-square" aria-hidden="true"></div>
      <div class="header-band header-band--contact">
        <span>info@qsc.example.au</span>
        <span>www.quillstonecompliance.example.au</span>
      </div>
      <p class="brand-name brand-name--letterhead">
        <span class="brand-name__line brand-name__line--main">Quillstone</span>
        <span class="brand-name__line brand-name__line--sub">Compliance</span>
      </p>
    </section>

    <section class="sheet sheet--cover" aria-label="Report cover">
      <div class="cover-graphic" role="img" aria-label="Large decorative brand graphic in slate grey and blue"></div>
      <p class="brand-name brand-name--cover">
        <span class="brand-name__line brand-name__line--main">Quillstone</span>
        <span class="brand-name__line brand-name__line--sub">Compliance</span>
      </p>
    </section>
  </main>
</body>
</html>
```